RMV Halvora BANK Website Design with UX/UI

I need a website DEV Design Mock up that can be presented in full HTML. Not code needed...just clickable design.
This is a BANk website.
We wil send some websites we like a bit later.
We need at least 10 pages that are Full HTML and integrated.
I will send more Design requirement details.
but feel free to go for it and be ahead

Hi
This is a Bank.
It will be based in the Caribbean. Please read up a bit about the Caribbean so you appreciate our region.
Therefore the only ethnicity that can be used is African American. Go to snapmeadow and search African American People so you can see the ethnicity of the people whom you must feature

The colour Scheme will be those of the Logo. The pantones were provided but it is the BLUE and Yellowish Orange

Target Market(s)

All Bank Customers

Industry/Entity Type

Banking

Number of Pages Required

5+ page

Colors
6b449b
ffc214

Requirements
Must have
• Logo
Follow the Brand Architecture
Use the Pantones provided
Follow the Suite Map Provided
Follow the brief Attached

```html
<!DOCTYPE html>
<html lang="en">
<head>
<meta charset="utf-8">
<title>RMV Halvora BANK</title>
<link href="https://fonts.googleapis.com/css2?family=Playfair+Display:wght@400;700&family=Montserrat:wght@400;600;700;800&family=Open+Sans:wght@400;600&display=swap" rel="stylesheet">
<style>
:root{
  --purple:#6b449b;
  --purple-dark:#3b1d68;
  --purple-deep:#2c1452;
  --yellow:#ffc214;
  --ink:#2a2a2a;
  --muted:#6d6d6d;
  --light:#f4f2f7;
  --white:#ffffff;
}
*{box-sizing:border-box;margin:0;padding:0}
html,body{width:1200px;height:3880px;overflow:hidden}
body{font-family:"Open Sans",Arial,sans-serif;color:var(--ink);background:var(--white);font-size:14px}
a{color:inherit;text-decoration:none}
.wrap{width:1090px;margin:0 auto;position:relative}

.topbar{height:32px;border-bottom:1px solid #e6e6e6;font-family:"Montserrat",sans-serif;font-size:11px;font-weight:600;color:var(--muted)}
.topbar .wrap{display:flex;justify-content:flex-end;gap:26px;align-items:center;height:32px}

.header{height:112px}
.header .wrap{display:flex;align-items:center;height:112px}
.brand{display:flex;align-items:center;gap:10px}
.brand-mark{width:30px;height:30px;border-radius:50%;background:var(--yellow);flex:none}
.brand-name{font-family:"Montserrat",sans-serif;font-weight:800;font-size:24px;color:var(--purple);letter-spacing:.5px;white-space:nowrap}
.search{margin-left:auto;display:flex;width:460px;height:32px;border:1px solid #ddd}
.search span{flex:1;padding:7px 12px;font-size:12px;color:#999}
.search b{width:34px;background:var(--yellow);display:flex;align-items:center;justify-content:center}
.login{margin-left:18px;height:32px;padding:0 18px;border:1px solid var(--purple);color:var(--purple);font-family:"Montserrat",sans-serif;font-size:12px;font-weight:700;display:flex;align-items:center}

.nav{height:40px;background:var(--purple)}
.nav .wrap{display:flex;height:40px;align-items:center}
.nav a{color:#fff;font-family:"Montserrat",sans-serif;font-size:12px;font-weight:600;padding:0 24px;height:40px;display:flex;align-items:center}
.nav a.active{background:var(--yellow);color:var(--purple-dark)}

.hero{height:436px;position:relative;background:linear-gradient(90deg,#f1f1f3 0%,#e4e2e8 45%,#c9c2d3 70%,#8f86a0 100%)}
.hero-photo{position:absolute;right:0;top:0;width:720px;height:436px;background:linear-gradient(100deg,rgba(240,240,243,0) 0%,#c6bccf 35%,#7e6b63 60%,#4b3a46 100%)}
.hero-text{position:absolute;left:110px;top:100px;width:500px}
.hero-kicker{font-family:"Montserrat",sans-serif;font-weight:700;font-size:17px;color:var(--purple);letter-spacing:.3px}
.hero-title{font-family:"Playfair Display",serif;font-size:34px;line-height:1.2;color:#333;margin-top:14px;font-weight:400}
.dots{position:absolute;left:110px;top:318px;display:flex;gap:6px}
.dots i{width:22px;height:5px;background:#d8d0e4;border-radius:3px}
.dots i:first-child{background:var(--yellow)}
.quick{position:absolute;right:0;top:88px;display:flex;flex-direction:column;gap:6px}
.quick a{width:160px;height:28px;background:#fff;color:var(--purple);font-family:"Montserrat",sans-serif;font-size:10px;font-weight:700;display:flex;align-items:center;padding-left:14px;box-shadow:0 2px 6px rgba(0,0,0,.15)}
.quick a:first-child{background:var(--purple);color:#fff}

.welcome{padding-top:88px;height:440px}
.welcome .wrap{display:flex;gap:40px}
.welcome-text{width:600px}
.title{font-family:"Playfair Display",serif;font-weight:700;font-size:22px;color:var(--purple);text-transform:uppercase;white-space:nowrap}
.title em{font-style:normal;color:var(--yellow)}
.welcome .title{font-size:19px}
.welcome-text p{font-size:12px;line-height:1.7;color:var(--muted);margin-top:18px}
.btn-purple{display:inline-flex;align-items:center;height:32px;padding:0 18px;background:var(--purple-dark);color:#fff;font-family:"Montserrat",sans-serif;font-weight:700;font-size:11px;margin-top:22px}
.tiles{display:grid;grid-template-columns:repeat(2,150px);gap:14px;margin-left:auto;margin-right:20px}
.tile{height:150px;background:var(--purple);color:#fff;font-family:"Montserrat",sans-serif;font-weight:700;font-size:11px;padding:18px 16px;display:flex;flex-direction:column;justify-content:flex-end;text-transform:uppercase;line-height:1.35}
.tile.dark{background:#1d1426}
.tile svg{margin-bottom:auto}
.tile span{color:var(--yellow)}

.tools{height:290px}
.tools .wrap{display:flex;gap:40px;justify-content:center}
.tool{width:474px;height:208px;border-radius:8px;position:relative;overflow:hidden}
.tool.mortgage{background:linear-gradient(120deg,#f2e8d6,#d9c6a4 50%,#a98d6a)}
.tool.currency{background:linear-gradient(120deg,#1e2f70,#2b4fa8 50%,#7e8fb8)}
.tool h3{position:absolute;top:22px;right:28px;font-family:"Playfair Display",serif;font-weight:700;font-size:20px;color:#fff;text-transform:uppercase;letter-spacing:.5px}
.tool.mortgage h3{color:var(--yellow)}
.tool .tag{position:absolute;top:62px;right:60px;background:#d4232b;color:#fff;font-family:"Montserrat",sans-serif;font-weight:700;font-size:12px;padding:6px 14px}

.moments{height:650px;background:linear-gradient(180deg,var(--purple-dark),var(--purple-deep));padding-top:66px}
.moments .title{color:#fff;text-align:center}
.moment-grid{display:grid;grid-template-columns:repeat(3,296px);gap:34px 58px;justify-content:center;margin-top:52px}
.moment .ph{height:160px;border:3px solid rgba(255,255,255,.85);position:relative}
.moment h4{font-family:"Montserrat",sans-serif;font-weight:700;font-size:14px;color:#fff;text-align:center;margin-top:12px;text-transform:uppercase}
.moment .learn{position:absolute;left:50%;top:50%;transform:translate(-50%,-50%);background:var(--yellow);color:var(--purple-dark);font-size:11px;font-weight:700;padding:6px 16px;font-family:"Montserrat",sans-serif}

.testimonials{height:740px;padding-top:70px;position:relative;overflow:hidden}
.testimonials .title{text-align:center}
.stage{position:relative;height:440px;margin-top:46px}
.t-main{position:absolute;left:288px;top:0;width:624px;height:440px;background:linear-gradient(135deg,#e7e2ec,#b6a9c4 40%,#5a4b5e 75%,#3a2f3e)}
.t-side{position:absolute;top:70px;width:240px;height:300px;opacity:.45}
.t-side.left{left:0;background:linear-gradient(135deg,#d7cde1,#8f7ca8)}
.t-side.right{right:0;background:linear-gradient(135deg,#e6dbed,#b8a4c9)}
.play{position:absolute;left:50%;top:50%;transform:translate(-50%,-50%)}
.t-side small{position:absolute;bottom:-38px;font-size:10px;color:#999}
.t-side.left small{right:8px;text-align:right}
.t-side.right small{left:8px}
.t-name{text-align:center;margin-top:24px;font-family:"Playfair Display",serif;font-weight:700;font-size:16px;color:var(--purple)}
.t-role{text-align:center;font-size:11px;color:var(--muted);margin-top:4px}
.view{display:flex;justify-content:center;margin-top:22px}
.view a{background:var(--purple);color:#fff;font-family:"Montserrat",sans-serif;font-size:11px;font-weight:700;padding:8px 18px}

.join{height:492px;background:linear-gradient(180deg,var(--purple-dark),var(--purple-deep));padding-top:74px;color:#fff}
.join .title{color:#fff;text-align:center}
.join .sub{text-align:center;font-size:13px;margin-top:8px;opacity:.9}
.form{width:632px;margin:34px auto 0;display:grid;grid-template-columns:1fr 1fr;gap:10px}
.field{height:34px;background:rgba(255,255,255,.12);border:1px solid rgba(255,255,255,.25);font-size:11px;padding:9px 12px;color:#e6def0}
.field.full{grid-column:1/3}
.field.msg{height:100px}
.submit{grid-column:2/3;justify-self:end;background:var(--yellow);color:var(--purple-dark);font-family:"Montserrat",sans-serif;font-weight:700;font-size:11px;padding:8px 14px;margin-top:4px}

.subscribe{height:68px;background:var(--yellow)}
.subscribe .wrap{display:flex;align-items:center;height:68px;padding-left:10px}
.subscribe h3{font-family:"Playfair Display",serif;font-weight:700;font-size:18px;color:var(--purple-dark)}
.sub-input{margin-left:auto;width:340px;height:32px;background:#fff;font-size:11px;color:#999;padding:9px 12px}
.sub-btn{height:32px;background:var(--purple);color:#fff;font-family:"Montserrat",sans-serif;font-weight:700;font-size:11px;padding:0 16px;display:flex;align-items:center;margin-right:110px}

.footer{height:432px;padding-top:42px;background:#fbfafc}
.footer .wrap{display:flex;gap:40px}
.f-brand{width:200px}
.f-brand .brand{flex-direction:column;align-items:flex-start;gap:8px}
.f-brand .brand-name{font-size:18px}
.f-brand p{font-size:11px;line-height:1.6;color:var(--muted);margin-top:16px}
.f-col h5{font-family:"Playfair Display",serif;font-weight:700;font-size:13px;color:var(--purple);margin-bottom:12px}
.f-col li{list-style:none;font-size:11px;color:var(--muted);line-height:1.95}
.social{position:absolute;right:60px;top:300px;display:flex;gap:8px}
.social i{width:26px;height:26px;border-radius:50%;background:var(--yellow)}
.copy{height:40px;background:var(--purple-dark);color:#d9cfe6;font-size:10px}
.copy .wrap{height:40px;display:flex;align-items:center;padding-left:10px}
</style>
</head>
<body>

<div class="topbar"><div class="wrap">
  <a>CHECKING</a><a>SAVINGS</a><a>CREDIT CARDS</a><a>LOANS</a><a>MORTGAGES</a><a>INVESTMENTS</a>
</div></div>

<header class="header"><div class="wrap">
  <div class="brand"><span class="brand-mark"></span><span class="brand-name">RMV Halvora BANK</span></div>
  <div class="search"><span>Search</span><b><svg width="14" height="14" viewBox="0 0 14 14"><circle cx="6" cy="6" r="4.5" fill="none" stroke="#3b1d68" stroke-width="1.8"/><line x1="9.3" y1="9.3" x2="13" y2="13" stroke="#3b1d68" stroke-width="1.8"/></svg></b></div>
  <a class="login">LOGIN / REGISTER</a>
</div></header>

<nav class="nav"><div class="wrap">
  <a class="active">HOME</a><a>PERSONAL</a><a>SMALL BUSINESS</a><a>PRIVATE BANKING</a><a>CORPORATE</a><a>WEALTH</a><a>ONLINE BANKING</a><a>CAREERS</a>
</div></nav>

<section class="hero">
  <div class="hero-photo" role="img" aria-label="Smiling bank advisor shaking hands with a client in a bright office"></div>
  <div class="hero-text">
    <div class="hero-kicker">YOUR SAFETY IS IMPORTANT TO US</div>
    <h1 class="hero-title">We Provide assistance for any<br>Covid-19 updates and policy<br>changes anytime</h1>
  </div>
  <div class="dots"><i></i><i></i><i></i><i></i></div>
  <div class="quick"><a>APPLY LOANS</a><a>ATM &amp; BRANCH</a><a>HELP &amp; SUPPORT</a></div>
</section>

<section class="welcome"><div class="wrap">
  <div class="welcome-text">
    <h2 class="title">Welcome to RMV Halvora <em>Banking Service</em></h2>
    <p>With our incorporation on March 3, 1994, as the Halvora Co-operative Bank Ltd, we became a registered public company with a strong share capital and the country's first locally owned bank. The Bank's operations started on May 9, 1994, at our former branch building in Port Meridel.</p>
    <p>In its early years, the Bank became well known for assisting entrepreneurs and small business owners who needed their operations to succeed. We allowed customers to open savings accounts with a small deposit, earning us the name "Little Vault" in our formative years.</p>
    <a class="btn-purple">LEARN MORE</a>
  </div>
  <div class="tiles">
    <div class="tile dark"><svg width="30" height="30" viewBox="0 0 30 30"><rect x="3" y="8" width="24" height="16" rx="2" fill="none" stroke="#ffc214" stroke-width="2"/><line x1="3" y1="13" x2="27" y2="13" stroke="#ffc214" stroke-width="2"/></svg>Open your<br>new account</div>
    <div class="tile"><svg width="30" height="30" viewBox="0 0 30 30"><path d="M4 19 L7 12 H23 L26 19 V23 H4 Z" fill="none" stroke="#fff" stroke-width="2"/><circle cx="9" cy="23" r="2" fill="#fff"/><circle cx="21" cy="23" r="2" fill="#fff"/></svg><span>Apply for<br>vehicle loan</span></div>
    <div class="tile"><svg width="30" height="30" viewBox="0 0 30 30"><path d="M4 15 L15 5 L26 15 M8 12 V25 H22 V12" fill="none" stroke="#fff" stroke-width="2"/></svg><span>Apply for<br>a mortgage</span></div>
    <div class="tile"><svg width="30" height="30" viewBox="0 0 30 30"><rect x="3" y="8" width="24" height="16" rx="2" fill="none" stroke="#fff" stroke-width="2"/><rect x="6" y="16" width="7" height="4" fill="#ffc214"/></svg><span>Apply for<br>credit card</span></div>
  </div>
</div></section>

<section class="tools"><div class="wrap">
  <div class="tool mortgage" role="img" aria-label="Model house with coins and a calculator"><h3>Mortgage Calculator</h3><span class="tag">CLICK HERE</span></div>
  <div class="tool currency" role="img" aria-label="Stacks of coins and banknotes over a city skyline"><h3>Online Currency Converter</h3><span class="tag">FIND OUT HERE</span></div>
</div></section>

<section class="moments">
  <h2 class="title">Part of every key moment of your life</h2>
  <div class="moment-grid">
    <div class="moment"><div class="ph" role="img" aria-label="Couple unpacking boxes in a new home" style="background:linear-gradient(135deg,#c9a85e,#8a6b3c)"><span class="learn">Learn More</span></div><h4>Starting a life together</h4></div>
    <div class="moment"><div class="ph" role="img" aria-label="House with a sold sign in the front yard" style="background:linear-gradient(135deg,#dfe4ea,#8a8f96)"></div><h4>Building your home</h4></div>
    <div class="moment"><div class="ph" role="img" aria-label="Family at a car dealership" style="background:linear-gradient(135deg,#e6e3e8,#9e96a6)"></div><h4>Buying your car</h4></div>
    <div class="moment"><div class="ph" role="img" aria-label="Newly married couple smiling outdoors" style="background:linear-gradient(135deg,#d9b88a,#7b5a3f)"></div><h4>Starting a life together</h4></div>
    <div class="moment"><div class="ph" role="img" aria-label="Family relaxing together in their living room" style="background:linear-gradient(135deg,#d8c8b0,#6f5c4c)"></div><h4>Building your home</h4></div>
    <div class="moment"><div class="ph" role="img" aria-label="Couple receiving keys to a new car" style="background:linear-gradient(135deg,#c9c1c5,#5e5358)"></div><h4>Buying your car</h4></div>
  </div>
</section>

<section class="testimonials">
  <h2 class="title">Testimonials from <em>happy customers</em></h2>
  <div class="stage">
    <div class="t-side left" role="img" aria-label="Customer testimonial video thumbnail"><svg class="play" width="50" height="50" viewBox="0 0 50 50"><circle cx="25" cy="25" r="23" fill="rgba(255,255,255,.7)"/><path d="M20 15 L35 25 L20 35 Z" fill="#6b449b"/></svg><small>Kerra Lindell<br>Teacher, Port Meridel</small></div>
    <div class="t-main" role="img" aria-label="Smiling customer in a shirt and tie at an office desk"><svg class="play" width="70" height="70" viewBox="0 0 70 70"><circle cx="35" cy="35" r="32" fill="rgba(255,255,255,.85)"/><path d="M28 21 L49 35 L28 49 Z" fill="#6b449b"/></svg></div>
    <div class="t-side right" role="img" aria-label="Customer testimonial video thumbnail"><svg class="play" width="50" height="50" viewBox="0 0 50 50"><circle cx="25" cy="25" r="23" fill="rgba(255,255,255,.7)"/><path d="M20 15 L35 25 L20 35 Z" fill="#6b449b"/></svg><small>Joel Marrin<br>Owner, Port Meridel</small></div>
  </div>
  <div class="t-name">Darnell Okafor Whitby</div>
  <div class="t-role">IT Sales Officer, Port Meridel</div>
  <div class="view"><a>VIEW ALL ›</a></div>
</section>

<section class="join">
  <h2 class="title">Join with us</h2>
  <p class="sub">Fill all the details. Our experts will reach you soon.</p>
  <div class="form">
    <div class="field">First Name</div><div class="field">Last Name</div>
    <div class="field">Email Address</div><div class="field">Phone Number</div>
    <div class="field full">Apply For</div>
    <div class="field full msg">Message ( Optional )</div>
    <a class="submit">APPLY NOW</a>
  </div>
</section>

<section class="subscribe"><div class="wrap">
  <h3>Subscribe here to Get Latest Updates</h3>
  <div class="sub-input">Enter your Email Address</div>
  <a class="sub-btn">SUBSCRIBE</a>
</div></section>

<footer class="footer"><div class="wrap">
  <div class="f-brand">
    <div class="brand"><span class="brand-mark"></span><span class="brand-name">RMV Halvora BANK</span></div>
    <p>To be the premier financial and related services provider to each client we serve world wide, creating wealth for all.</p>
  </div>
  <div class="f-col"><h5>Main Links</h5><ul><li>Personal</li><li>Small Business</li><li>Private Banking</li><li>Corporate</li><li>Wealth</li><li>Online Banking</li><li>ATM &amp; Branch</li><li>Careers</li></ul></div>
  <div class="f-col"><h5>Personal</h5><ul><li>Checking</li><li>Savings</li><li>Credit Cards</li><li>Loans</li><li>Mortgages</li><li>Investments</li><li>Instant Apply</li><li>Rates</li></ul></div>
  <div class="f-col"><h5>Calculator</h5><ul><li>Mortgage Loan</li><li>Car Loan</li><li>Personal Loan</li><li>Renovation Loan</li><li>Business Loan</li></ul></div>
  <div class="f-col"><h5>About Us</h5><ul><li>Our Story</li><li>Investor Relations</li><li>Security Center</li><li>Customer Service</li><li>Newsroom</li></ul></div>
  <div class="f-col"><h5>Customer Support</h5><ul><li>Help &amp; Support</li><li>Contact Us</li><li>Terms and Conditions</li><li>Privacy Policy</li><li>Sitemap</li></ul></div>
  <div class="social"><i></i><i></i><i></i><i></i><i></i></div>
</div></footer>

<div class="copy"><div class="wrap">RMV Halvora BANK © Copyright 2020 All Rights Reserved</div></div>

</body>
</html>
```